Hipster Hard Apple Cider - Bike / Gear / Cog Themed Label

Hard Apple Cider Label Needed:

- Looking for a retro, fun, funky, Venice Beach vibe.

- Design should incorporate bike/bicycle/wheel elements, appeal to both sexes and should be applicable to a can. (See can example in attachments).

- There should be a main brand logo that can stand alone in representing the brand and the feel of the brand. I envision a bike wheel, Sp*kes, gears, etc.

Please use brand name posted as JPG titled "Brand Name" in Attached Files:
>>> Brindle Cider

Target Market(s)

Our consumer is:
- Millennial
- Hipster
- Adventurous
- Active (biking/cycling)
- A craft beer + wine purchaser
- Unisex, veering towards masculine (65% male)

Industry/Entity Type

Wheel

Requirements
Must have
• - Bike elements that tie in the brand name (cogs, sp*kes, gears, bike frame, etc.)
• - A strong logo that can represent the brand

```html
<!DOCTYPE html>
<html lang="en">
<head>
<meta charset="utf-8">
<title>Brindle Cider – Hard Apple Cider Labels</title>
<link rel="stylesheet" href="https://fonts.googleapis.com/css2?family=Oswald:wght@500&family=Lobster&display=swap">
<style>
  :root {
    --page-bg: #eeeff2;
    --label-bg: #ffffff;
    --brand-orange: #e8501e;
    --olive: #6e6410;
    --bike-tone: #f2b79e;
  }
  * { box-sizing: border-box; margin: 0; padding: 0; }
  html, body {
    width: 1200px;
    height: 1040px;
    overflow: hidden;
    background: var(--page-bg);
  }
  .canvas {
    width: 1200px;
    height: 1040px;
    display: flex;
    justify-content: space-between;
    padding: 40px 48px;
  }
  .label {
    width: 504px;
    height: 960px;
    background: var(--label-bg);
    display: flex;
    flex-direction: column;
    align-items: center;
    position: relative;
    box-shadow: 0 2px 10px rgba(0,0,0,0.06);
  }
  .brand {
    margin-top: 80px;
    display: flex;
    align-items: center;
    gap: 16px;
    font-family: "Oswald", sans-serif;
    font-weight: 500;
    font-size: 44px;
    letter-spacing: 1px;
    color: var(--brand-orange);
    text-transform: uppercase;
  }
  .brand-dot {
    width: 22px;
    height: 22px;
    border-radius: 50%;
    background: var(--brand-orange);
  }
  .divider {
    width: 330px;
    height: 2px;
    background: var(--olive);
  }
  .divider-top { margin-top: 126px; }
  .product-name {
    margin-top: 28px;
    font-family: "Lobster", cursive;
    color: var(--olive);
    font-size: 104px;
    line-height: 0.86;
    text-align: center;
  }
  .variant {
    margin-top: 18px;
    border: 2px solid var(--olive);
    padding: 2px 10px;
    font-family: "Oswald", sans-serif;
    font-weight: 500;
    font-size: 24px;
    letter-spacing: 1px;
    color: var(--olive);
    text-transform: uppercase;
  }
  .divider-bottom { position: absolute; top: 678px; }
  .abv {
    position: absolute;
    top: 756px;
    font-family: "Oswald", sans-serif;
    font-weight: 500;
    font-size: 15px;
    color: var(--brand-orange);
  }
  .bike-art {
    position: absolute;
    top: 786px;
    width: 122px;
    height: 74px;
    border-radius: 6px;
    background: var(--bike-tone);
  }
  .volume {
    position: absolute;
    top: 900px;
    font-family: "Oswald", sans-serif;
    font-weight: 500;
    font-size: 14px;
    color: var(--brand-orange);
  }
</style>
</head>
<body>
<main class="canvas">
  <section class="label label-chardonnay">
    <div class="brand"><span>Brindle</span><span class="brand-dot"></span><span>Cider</span></div>
    <div class="divider divider-top"></div>
    <h1 class="product-name">Hard<br>Apple<br>Cider</h1>
    <p class="variant">Chardonnay Barrel Aged</p>
    <div class="divider divider-bottom"></div>
    <p class="abv">7% ALC./VOL</p>
    <div class="bike-art" role="img" aria-label="Orange line illustration of a racing bicycle with two small birds above"></div>
    <p class="volume">330 ML</p>
  </section>

  <section class="label label-dry">
    <div class="brand"><span>Brindle</span><span class="brand-dot"></span><span>Cider</span></div>
    <div class="divider divider-top"></div>
    <h1 class="product-name">Hard<br>Apple<br>Cider</h1>
    <p class="variant">Dry</p>
    <div class="divider divider-bottom"></div>
    <p class="abv">7% ALC./VOL</p>
    <div class="bike-art" role="img" aria-label="Orange line illustration of a racing bicycle with two small birds above"></div>
    <p class="volume">330 ML</p>
  </section>
</main>
</body>
</html>
```